New Business Card for Auto Repair and Performance Shop!

Need a redesign on a card that we have used for a while now. Something more update and modern, Serious but not too serious. Something confident, that shows the client that we are bespoke. Adding value.

Target Market(s)

Foreign Auto Repair and Performance

Industry/Entity Type

Automotive

Contact Information for Business Card

Utilize Logo, would like to change car silhouette to something Veltra,

Font styles to use
Sans Serif

Requirements
Must have
• business name, address, website, phone number.
MotoSerenix
4918 W. Birchwell Rd
Harlowe, T.X. 70811
1-555-487-3106
www.moto-serenix-example.com

Specializing in Asian, European, and Domestic Auto Repair, Performance and Fabrication.

Clear space on back to for space to write appointment time and which client advisor helped the client.
Nice to have
• Up to the designers,

```html
<!DOCTYPE html>
<html lang="en">
<head>
<meta charset="utf-8">
<title>MotoSerenix Business Card</title>
<link rel="stylesheet" href="https://fonts.googleapis.com/css2?family=Arimo:wght@400;700&family=Open+Sans:wght@300;400&family=Roboto+Condensed:wght@700&display=swap">
<style>
  :root {
    --board: #373435;
    --card: #ffffff;
    --ink: #373435;
    --brand-red: #b02a30;
    --divider: #e4e4e4;
    --label: #ffffff;
  }
  * { margin: 0; padding: 0; box-sizing: border-box; }
  html, body { width: 924px; height: 1200px; overflow: hidden; }
  body { background: var(--board); position: relative; font-family: "Open Sans", sans-serif; color: var(--ink); }

  .board-title {
    position: absolute; top: 128px; left: 0; width: 946px; text-align: center;
    font-family: "Arimo", sans-serif; font-weight: 700; font-size: 52px; color: var(--label);
  }
  .side-label {
    position: absolute; font-family: "Arimo", sans-serif; font-weight: 700; font-size: 30px; color: var(--label);
  }
  .side-label--front { left: 34px; top: 388px; }
  .side-label--back { left: 42px; top: 831px; }

  .card { position: absolute; background: var(--card); width: 673px; height: 402px; }
  .card--front { left: 150px; top: 215px; }
  .card--back { left: 152px; top: 657px; }

  .brand-mark {
    position: absolute; left: 71px; top: 86px; width: 214px; height: 214px;
    border: 3px solid var(--ink); border-radius: 50%;
    display: flex; align-items: center; justify-content: center;
  }
  .brand-name { font-family: "Open Sans", sans-serif; font-weight: 400; font-size: 30px; color: var(--ink); }

  .divider { position: absolute; left: 336px; top: 54px; width: 1px; height: 264px; background: var(--divider); }

  .person { position: absolute; left: 364px; top: 37px; }
  .person-name { font-weight: 400; font-size: 29px; letter-spacing: 0.5px; line-height: 36px; }
  .person-role { font-weight: 400; font-size: 21px; line-height: 28px; }

  .contact-list { position: absolute; left: 364px; top: 163px; list-style: none; }
  .contact-item { display: flex; align-items: flex-start; font-size: 19.5px; line-height: 27.5px; white-space: nowrap; }
  .contact-item + .contact-item { margin-top: 0.5px; }
  .contact-item--web { font-size: 17px; }
  .contact-icon { width: 20px; height: 20px; margin: 4px 12px 0 0; flex: none; fill: none; stroke: var(--brand-red); stroke-width: 1.6; }
  .contact-icon--solid { fill: var(--brand-red); stroke: none; }

  .tagline-band {
    position: absolute; left: 0; top: 345px; width: 100%; height: 37px; background: var(--brand-red);
    display: flex; align-items: center; justify-content: center;
    font-family: "Roboto Condensed", sans-serif; font-weight: 700; font-size: 17.5px; color: #fff;
  }

  .write-box { position: absolute; top: 284px; height: 76px; border: 2.5px solid var(--ink); }
  .write-box--time { left: 26px; width: 152px; }
  .write-box--advisor { left: 189px; width: 460px; }
  .write-box-head {
    height: 27px; background: var(--ink); color: #fff;
    font-family: "Arimo", sans-serif; font-size: 16.5px; line-height: 25px; text-align: center;
  }
</style>
</head>
<body>
  <h1 class="board-title">BUSINESS CARD</h1>
  <div class="side-label side-label--front">FRONT</div>
  <div class="side-label side-label--back">BACK</div>

  <section class="card card--front">
    <div class="brand-mark"><span class="brand-name">MotoSerenix</span></div>
    <div class="divider"></div>

    <div class="person">
      <p class="person-name">NAME SURNAME</p>
      <p class="person-role">Sales Manager</p>
    </div>

    <ul class="contact-list">
      <li class="contact-item">
        <svg class="contact-icon" viewBox="0 0 20 20"><rect x="5" y="1.5" width="10" height="17" rx="2"/><line x1="8.5" y1="4" x2="11.5" y2="4"/><circle cx="10" cy="15.5" r="0.8"/></svg>
        1-555-487-3106
      </li>
      <li class="contact-item">
        <svg class="contact-icon" viewBox="0 0 20 20"><rect x="1.5" y="4" width="17" height="12"/><polyline points="1.5,4 10,11 18.5,4"/><line x1="1.5" y1="16" x2="8" y2="9.5"/><line x1="18.5" y1="16" x2="12" y2="9.5"/></svg>
        email@domain.com
      </li>
      <li class="contact-item contact-item--web">
        <svg class="contact-icon" viewBox="0 0 20 20"><circle cx="10" cy="10" r="8.5"/><ellipse cx="10" cy="10" rx="4" ry="8.5"/><line x1="1.5" y1="10" x2="18.5" y2="10"/><line x1="3" y1="5.5" x2="17" y2="5.5"/><line x1="3" y1="14.5" x2="17" y2="14.5"/></svg>
        www.moto-serenix-example.com
      </li>
      <li class="contact-item">
        <svg class="contact-icon contact-icon--solid" viewBox="0 0 20 20"><path d="M10 1a7 7 0 0 0-7 7c0 5 7 11 7 11s7-6 7-11a7 7 0 0 0-7-7zm0 9.5a2.7 2.7 0 1 1 0-5.4 2.7 2.7 0 0 1 0 5.4z"/></svg>
        <span>4918 W. Birchwell Rd<br>Harlowe, T.X. 70811</span>
      </li>
    </ul>

    <div class="tagline-band">Specializing in Asian, European, and Domestic Auto Repair, Performance and Fabrication.</div>
  </section>

  <section class="card card--back">
    <div class="write-box write-box--time"><div class="write-box-head">Appointment Time</div></div>
    <div class="write-box write-box--advisor"><div class="write-box-head">Client Advisor Name</div></div>
  </section>
</body>
</html>
```